Business Card phone number change

This one should be easy, and I've committed to pay even is takes you minutes to complete.
I have a completed business card for which I just need a phone number changed. It needs to be done asap (within hours) so I can have it printed today. I have the card design and everything. Literally just need phone number changed and positioned in correct place. If you can do it, let me know.
The card was originally designed with 3.62” x 2.12” . It was modified to US standard 3.5” x 2” (which is how I need it).

On the file named "Final TM Partners card size" the NY number should read +1 212 555 0147" rather than the 212 555 0183 number that is there. If you can do let, let me now ASAP.
Updates

Project Deadline Extended Reason: The deadling is today, 4 hours from initial posting. Short window as all that needs to be changed is the phone number and I need to print a stack today before meeting. Added Saturday, January 14, 2017

Industry/Entity Type

Business

Requirements
Must have
• The correct NY phone number of +1 212 555 0147
• Everything else stays the same.

```html
<!DOCTYPE html>
<html lang="en">
<head>
<meta charset="utf-8">
<title>TM Partners – Business Card</title>
<link rel="stylesheet" href="https://fonts.googleapis.com/css2?family=Noto+Serif:wght@400;700&display=swap">
<style>
  :root {
    --ink: #3a5273;
    --muted: #9a9a9a;
    --crop: #8c8c8c;
    --paper: #ffffff;
  }
  * { margin: 0; padding: 0; box-sizing: border-box; }
  html, body {
    width: 1200px;
    height: 848px;
    overflow: hidden;
    background: var(--paper);
  }
  .sheet {
    position: relative;
    width: 1200px;
    height: 848px;
    font-family: "Noto Serif", Georgia, serif;
    color: var(--ink);
  }
  .crop-marks { position: absolute; left: 0; top: 0; }

  .brand {
    position: absolute;
    left: 606px;
    top: 331px;
    display: flex;
    align-items: center;
    gap: 8px;
  }
  .brand-dot {
    width: 42px;
    height: 42px;
    border-radius: 50%;
    background: var(--ink);
  }
  .brand-name {
    font-weight: 700;
    font-size: 17px;
    letter-spacing: 0.2px;
    color: var(--ink);
  }

  .address {
    position: absolute;
    right: 440px;
    top: 367px;
    text-align: right;
    font-size: 9.5px;
    line-height: 12.5px;
  }

  .identity {
    position: absolute;
    left: 483px;
    top: 403px;
  }
  .person-name {
    font-weight: 700;
    font-size: 13.5px;
    line-height: 16px;
  }
  .person-role {
    font-size: 12.5px;
    line-height: 15px;
  }

  .rule {
    position: absolute;
    left: 479px;
    width: 319px;
    height: 4px;
    background: var(--ink);
  }
  .rule-top { top: 443px; }
  .rule-bottom { top: 505px; }

  .contacts {
    position: absolute;
    left: 420px;
    top: 451px;
    display: grid;
    grid-template-columns: 54px auto;
    column-gap: 9px;
    font-size: 9.5px;
    line-height: 12.6px;
  }
  .contact-label { text-align: right; color: var(--muted); }
  .contact-value { color: var(--ink); }
</style>
</head>
<body>
<main class="sheet">
  <svg class="crop-marks" width="1200" height="848" viewBox="0 0 1200 848" aria-hidden="true">
    <g stroke="var(--crop)" stroke-width="1">
      <line x1="415.5" y1="260" x2="415.5" y2="298"/>
      <line x1="771.5" y1="260" x2="771.5" y2="298"/>
      <line x1="415.5" y1="542" x2="415.5" y2="580"/>
      <line x1="771.5" y1="542" x2="771.5" y2="580"/>
      <line x1="357" y1="318.5" x2="397" y2="318.5"/>
      <line x1="792" y1="318.5" x2="832" y2="318.5"/>
      <line x1="357" y1="521.5" x2="397" y2="521.5"/>
      <line x1="792" y1="521.5" x2="832" y2="521.5"/>
    </g>
  </svg>

  <div class="brand">
    <span class="brand-dot"></span>
    <span class="brand-name">TM Partners</span>
  </div>

  <address class="address" style="font-style:normal">
    48 Harbor Lane<br>
    Brooklyn, NY 11201
  </address>

  <div class="identity">
    <p class="person-name">Alex Moreno</p>
    <p class="person-role">Healthcare Consultant</p>
  </div>

  <div class="rule rule-top"></div>

  <div class="contacts">
    <span class="contact-label">New York:</span>
    <span class="contact-value">+1 212 555 0147</span>
    <span class="contact-label">Madrid:</span>
    <span class="contact-value">+34 600 555 012</span>
    <span class="contact-label">Email:</span>
    <span class="contact-value">amoreno@tmpartners.com</span>
    <span class="contact-label">Web:</span>
    <span class="contact-value">www.tmpartners.com</span>
  </div>

  <div class="rule rule-bottom"></div>
</main>
</body>
</html>
```